Bold & Clean Birch Harbor Stationary Design

Our company, Birch Harbor Advisory Partners needs a business card, letterhead, and envelope design that all also the formatting standards for quillpressdepot.com.

Envelope:
Safe Zone: 9.375" x 4"
Trim Size: 9.5" x 4.15"
Bleed Size: 11.125" 8.625"

Letterhead:
Safe Zone: 10.875" x 8.375"
Trim Size: 11" x 8.5"
Bleed Size: 11.125" x 8.625"

Our mailing address is:
7318 W Larkmoor Rd
Chicago, IL 60647

Please make sure the return address on the envelope is formatted correctly for mailing and the logo is not too large.

Please submit designs in word and PDF form.

Our current letterhead is attached.

We would also like a business card with our existing logo that will meet standards for formatting through Quill Press Depot (quillpressdepot.com).

These standards are:
Safe Zone: 3.375" x 1.875"
Trim Size: 3.5" x 2"
Bleed Size: 3.625" x 2.125"

The business card is going to be for Marcus Lindqvist, President/CEO of Birch Harbor Advisory Partners. Please include the Address, Telephone Number, Cell Phone Number, Fax Number, Email, and Website Address on the card, which are as follows:

7318 W Larkmoor Rd
Chicago, IL 60647

Tel: (773) 591-3072
Cell: (630) 287-6093
Fax: (63) 417-2058
Email: mjl@birchharboradvisory.com
Web: www.birchharboradvisory.com

Please make sure that we can easily change the name of the staff member and job position title ourselves as we will be having cards for individual employees in the future as well.

The back of the card should also have the Birch Harbor logo on it with our services listed:

Financial Planning | Tax | Solutions for Small Businesses

Industry/Entity Type

Accounting

Requirements
Must have
• envelope
• letterhead
• business card
• All meeting standards set out above.

```html
<!DOCTYPE html>
<html lang="en">
<head>
<meta charset="utf-8">
<title>Birch Harbor Stationery</title>
<link href="https://fonts.googleapis.com/css2?family=Roboto:wght@400;500&family=Open+Sans:wght@400;600&display=swap" rel="stylesheet">
<style>
:root{
  --navy:#1e2d5c;
  --orange:#f05a28;
  --backdrop:#bdbdbd;
  --paper:#ffffff;
  --faint-navy:#dfe1e8;
  --faint-orange:#fbe4dc;
}
*{box-sizing:border-box;margin:0;padding:0}
html,body{width:1200px;height:1200px;overflow:hidden;background:var(--backdrop)}
body{position:relative;font-family:'Roboto',sans-serif;color:var(--navy)}
.sheet{position:absolute;background:var(--paper);box-shadow:8px 10px 12px rgba(0,0,0,.45);overflow:hidden}
.brand{display:flex;align-items:center;gap:6px;color:var(--navy);font-family:'Roboto',sans-serif;font-weight:500;white-space:nowrap}
.brand-dot{border-radius:50%;border:2px solid var(--navy);flex:none}
.divider{position:absolute;width:1px;background:var(--orange)}
.name{font-size:11px;font-weight:500;white-space:nowrap}
.title{font-size:6.5px;margin-top:2px;white-space:nowrap}
.contacts{font-size:7.4px;line-height:11px}
.contacts li{list-style:none;display:flex;align-items:center;gap:6px;white-space:nowrap}
.contacts .gap{margin-top:5px}
.icon{width:7px;height:7px;flex:none}
.services{position:absolute;font-size:8.2px;white-space:nowrap}
.services i{font-style:normal;margin:0 4px}
.return-address{position:absolute;font-size:7.6px;line-height:10px;white-space:nowrap}
.faint-mark{position:absolute;border-radius:50%;border:4px solid var(--faint-navy)}
.faint-mark::after{content:"";position:absolute;inset:28%;border-radius:50%;background:var(--faint-orange)}
.band{position:absolute;left:0;right:0;background:var(--navy)}
.band-accent{position:absolute;left:0;top:0;bottom:0;background:var(--orange)}
.letter-body{position:absolute;left:47px;top:113px;width:415px;font-family:'Open Sans',sans-serif;font-size:7.6px;line-height:17px;color:#222}
.letter-body h2{font-size:8px;font-weight:600;color:#000;margin-bottom:17px}
.letter-body p{margin-bottom:17px}
.signature{width:125px;height:42px;margin:4px 0 6px;background:linear-gradient(90deg,#f3f3f3,#e6e6e6);border-radius:3px}
.letter-footer{position:absolute;left:0;right:0;bottom:0;height:33px;background:var(--navy);color:#fff;font-size:6.6px}
.letter-footer .services{left:0;right:0;top:5px;text-align:center;font-size:7px;padding-left:46px}
.footer-contacts{position:absolute;left:72px;top:19px;display:flex;gap:11px;white-space:nowrap;align-items:center}
.footer-contacts span{display:flex;align-items:center;gap:4px}
.flap{position:absolute;left:0;top:0;width:100%;height:60px}
</style>
</head>
<body>

<!-- Business card: text-only front -->
<div class="sheet card" style="left:48px;top:58px;width:254px;height:144px">
  <div style="position:absolute;right:154px;top:70px;text-align:right">
    <div class="name">Marcus Lindqvist</div>
    <div class="title">President/CEO</div>
  </div>
  <div class="divider" style="left:114px;top:44px;height:84px"></div>
  <ul class="contacts" style="position:absolute;left:127px;top:51px">
    <li><svg class="icon" viewBox="0 0 10 10"><path d="M1 4h8v5H1zM2 1h6v2H2z" fill="#f05a28"/></svg>(773) 591-3072</li>
    <li><svg class="icon" viewBox="0 0 10 10"><rect x="1" y="3" width="8" height="6" fill="#f05a28"/></svg>(630) 287-6093</li>
    <li class="gap"><svg class="icon" viewBox="0 0 10 10"><path d="M1 2h8v6H1z M1 2l4 3 4-3" fill="none" stroke="#f05a28" stroke-width="1.4"/></svg>mjl@birchharboradvisory.com</li>
    <li><svg class="icon" viewBox="0 0 10 10"><circle cx="5" cy="5" r="4" fill="none" stroke="#f05a28" stroke-width="1.4"/></svg>www.birchharboradvisory.com</li>
  </ul>
  <div class="return-address" style="left:127px;top:107px;font-size:8.4px;line-height:11px">7318 W Larkmoor Rd<br>Chicago, IL 60647</div>
</div>

<!-- Business card: mark + contacts -->
<div class="sheet card" style="left:48px;top:237px;width:254px;height:144px">
  <div class="brand" style="position:absolute;left:20px;top:66px;font-size:10px"><span class="brand-dot" style="width:16px;height:16px"></span>Birch Harbor</div>
  <div class="divider" style="left:112px;top:20px;height:108px"></div>
  <div style="position:absolute;left:124px;top:28px">
    <div class="name">Marcus Lindqvist</div>
    <div class="title">President/CEO</div>
  </div>
  <ul class="contacts" style="position:absolute;left:124px;top:67px">
    <li><svg class="icon" viewBox="0 0 10 10"><path d="M1 4h8v5H1zM2 1h6v2H2z" fill="#f05a28"/></svg>(773) 591-3072</li>
    <li><svg class="icon" viewBox="0 0 10 10"><rect x="1" y="3" width="8" height="6" fill="#f05a28"/></svg>(630) 287-6093</li>
    <li class="gap"><svg class="icon" viewBox="0 0 10 10"><path d="M1 2h8v6H1z M1 2l4 3 4-3" fill="none" stroke="#f05a28" stroke-width="1.4"/></svg>mjl@birchharboradvisory.com</li>
    <li><svg class="icon" viewBox="0 0 10 10"><circle cx="5" cy="5" r="4" fill="none" stroke="#f05a28" stroke-width="1.4"/></svg>www.birchharboradvisory.com</li>
  </ul>
</div>

<!-- Business card back: white -->
<div class="sheet card" style="left:331px;top:237px;width:254px;height:144px">
  <div class="brand" style="position:absolute;left:30px;top:40px;font-size:20px"><span class="brand-dot" style="width:26px;height:26px"></span>Birch Harbor</div>
  <div class="services" style="left:0;right:0;top:112px;text-align:center">Financial Planning<i>|</i>Tax<i>|</i>Solutions for Small Businesses</div>
</div>

<!-- Business card: header layout -->
<div class="sheet card" style="left:48px;top:422px;width:254px;height:144px">
  <div class="brand" style="position:absolute;left:14px;top:11px;font-size:9px"><span class="brand-dot" style="width:13px;height:13px"></span>Birch Harbor</div>
  <div style="position:absolute;right:15px;top:13px;text-align:left">
    <div class="name">Marcus Lindqvist</div>
    <div class="title">President/CEO</div>
  </div>
  <ul class="contacts" style="position:absolute;left:15px;top:53px">
    <li><svg class="icon" viewBox="0 0 10 10"><path d="M1 4h8v5H1zM2 1h6v2H2z" fill="#f05a28"/></svg>(773) 591-3072</li>
    <li><svg class="icon" viewBox="0 0 10 10"><rect x="1" y="3" width="8" height="6" fill="#f05a28"/></svg>(630) 287-6093</li>
    <li class="gap"><svg class="icon" viewBox="0 0 10 10"><path d="M1 2h8v6H1z M1 2l4 3 4-3" fill="none" stroke="#f05a28" stroke-width="1.4"/></svg>mjl@birchharboradvisory.com</li>
    <li><svg class="icon" viewBox="0 0 10 10"><circle cx="5" cy="5" r="4" fill="none" stroke="#f05a28" stroke-width="1.4"/></svg>www.birchharboradvisory.com</li>
  </ul>
  <div class="return-address" style="left:15px;top:107px;font-size:8.4px;line-height:10px">7318 W Larkmoor Rd<br>Chicago, IL 60647</div>
  <div class="band" style="bottom:0;height:11px"><span class="band-accent" style="width:40px"></span></div>
</div>

<!-- Business card back: navy -->
<div class="sheet card" style="left:331px;top:422px;width:254px;height:144px;background:var(--navy)">
  <div class="brand" style="position:absolute;left:30px;top:42px;font-size:20px;color:#fff"><span class="brand-dot" style="width:26px;height:26px;border-color:#fff"></span>Birch Harbor</div>
  <div class="services" style="left:0;right:0;top:118px;text-align:center;color:#fff">Financial Planning<i>|</i>Tax<i>|</i>Solutions for Small Businesses</div>
</div>

<!-- Envelope front with band -->
<div class="sheet envelope" style="left:29px;top:651px;width:556px;height:242px">
  <div class="brand" style="position:absolute;left:14px;top:14px;font-size:10px"><span class="brand-dot" style="width:15px;height:15px"></span>Birch Harbor</div>
  <div class="return-address" style="left:16px;top:50px">7318 W Larkmoor Rd<br>Chicago, IL 60647</div>
  <div class="faint-mark" style="left:382px;top:91px;width:150px;height:150px"></div>
  <div class="band" style="top:219px;height:23px"><span class="band-accent" style="width:52px"></span></div>
</div>

<!-- Envelope front plain -->
<div class="sheet envelope" style="left:28px;top:930px;width:557px;height:243px">
  <div class="brand" style="position:absolute;left:14px;top:20px;font-size:10px"><span class="brand-dot" style="width:15px;height:15px"></span>Birch Harbor</div>
  <div class="return-address" style="left:16px;top:51px">7318 W Larkmoor Rd<br>Chicago, IL 60647</div>
  <div class="faint-mark" style="left:382px;top:91px;width:150px;height:150px"></div>
</div>

<!-- Envelope back -->
<div class="sheet envelope" style="left:612px;top:930px;width:557px;height:243px">
  <svg class="flap" viewBox="0 0 557 60" preserveAspectRatio="none"><path d="M0 0 L70 56 H487 L557 0" fill="none" stroke="#b9bcc8" stroke-width="1"/></svg>
  <div class="brand" style="position:absolute;left:259px;top:13px;font-size:0"><span class="brand-dot" style="width:20px;height:20px"></span></div>
  <div class="brand" style="position:absolute;left:0;right:0;top:36px;justify-content:center;font-size:7px">Birch Harbor</div>
</div>

<!-- Letterhead -->
<div class="sheet letterhead" style="left:671px;top:252px;width:498px;height:643px">
  <div class="brand" style="position:absolute;left:175px;top:33px;font-size:14px"><span class="brand-dot" style="width:22px;height:22px"></span>Birch Harbor</div>
  <div class="faint-mark" style="left:253px;top:400px;width:200px;height:200px"></div>
  <div class="letter-body">
    <h2>Lorem Ipsum is simply</h2>
    <p>dummy text of the printing and typesetting industry. Lorem Ipsum has been the industry's standard dummy text ever since the 1500s, when an unknown printer took a galley of type and scrambled it to make a type specimen book. It has survived not only five centuries, but also the leap into electronic typesetting, remaining essentially unchanged. It was popularised in the 1960s with the release of Typeline sheets containing Lorem Ipsum passages, and more recently with desktop publishing software like Foliant PageSetter including versions of Lorem Ipsum.</p>
    <p>It is a long established fact that a reader will be distracted by the readable content of a page when looking at its layout. The point of using Lorem Ipsum is that it has a more-or-less normal distribution of letters, as opposed to using 'Content here, content here', making it look like readable English. Many desktop publishing packages and web page editors now use Lorem Ipsum as their default model text, and a search for 'lorem ipsum' will uncover many web sites still in their infancy. Various versions have evolved over the years, sometimes by accident, sometimes on purpose (injected humour and the like).</p>
    <p style="margin-bottom:14px">Contrary to popular belief, Lorem Ipsum is not simply random text. It has roots in a piece of classical Latin literature from 45 BC, making it over 2000 years old. Walter Pennington, a Latin professor at Larkfield College in Virginia, looked up one of the more obscure Latin words, consectetur, from a Lorem Ipsum passage,</p>
    <div>Lorem Ipsum</div>
    <div class="signature" role="img" aria-label="Handwritten signature"></div>
    <div>Lorem Ipsum is a dummy</div>
  </div>
  <footer class="letter-footer">
    <span class="band-accent" style="width:46px"></span>
    <div class="services">Financial Planning<i>|</i>Tax<i>|</i>Solutions for Small Businesses</div>
    <div class="footer-contacts">
      <span><svg class="icon" viewBox="0 0 10 10"><circle cx="5" cy="5" r="5" fill="#f05a28"/></svg>(773) 591-3072</span>
      <span><svg class="icon" viewBox="0 0 10 10"><circle cx="5" cy="5" r="5" fill="#f05a28"/></svg>(630) 287-6093</span>
      <span><svg class="icon" viewBox="0 0 10 10"><circle cx="5" cy="5" r="5" fill="#f05a28"/></svg>www.birchharboradvisory.com</span>
      <span style="border-left:1px solid #fff;padding-left:8px">7318 W Larkmoor Rd, Chicago, IL 60647</span>
    </div>
  </footer>
</div>

</body>
</html>
```